I have a logo and need to design the business card and stationery.
Updates

The uploaded logo image named as GREYHAVEN CONSTRUCTION which is to be replaced to GREYHAVEN CONTRACTS. Kindly add below details and submit the designs- Company name- Greyhaven Engineering Contracts LLP Name & Post- Kunal Mehra (Designated Partner) Address- Block No.317, Wing C, Tulsi Trade Plaza, Lokhand Marg, Varun Industrial Park, Goregaon(E), Mumbai - 400 063 Contact- +91 97410 58723 Email- kunalmehra@examplemail.com Website- www.greyhavencontracts.example Contact for Letterhead- +91-22-28145597

Hi Tanvir Rahman, We are liking your Design #41927506. We have suggested some changes which are mentioned in feedback. Kindly revert with it asap to finalize this design.

Colors

Designer to choose colors to be used in the design.

```html
<!DOCTYPE html>
<html lang="en">
<head>
<meta charset="utf-8">
<title>Greyhaven Contracts — Business Card</title>
<link rel="stylesheet" href="https://fonts.googleapis.com/css2?family=Montserrat:wght@400;500;700;800&display=swap">
<style>
  :root {
    --bg: #d6d6d6;
    --card-white: #ffffff;
    --charcoal: #333335;
    --ink: #2b2b2d;
    --muted: #4a4a4c;
    --back-mark: #58585b;
  }
  * { margin: 0; padding: 0; box-sizing: border-box; }
  html, body {
    width: 1200px; height: 848px; overflow: hidden;
    background: var(--bg);
    font-family: "Montserrat", Arial, sans-serif;
  }
  .stage {
    position: relative; width: 1200px; height: 848px;
    display: flex; align-items: center; justify-content: center; gap: 48px;
  }
  .card {
    position: relative; width: 520px; height: 300px; overflow: hidden;
    box-shadow: 0 10px 28px rgba(0,0,0,0.18);
  }
  /* Front */
  .card--front { background: var(--card-white); color: var(--ink); }
  .front__panel {
    position: absolute; left: 0; top: 128px; width: 228px; height: 172px;
    background: var(--charcoal);
  }
  .front__content {
    position: absolute; left: 250px; top: 30px; right: 24px;
    display: flex; flex-direction: column; align-items: flex-start;
  }
  .brand {
    display: flex; align-items: center; gap: 10px; margin-bottom: 22px;
  }
  .brand__square { width: 22px; height: 22px; background: var(--ink); }
  .brand__name {
    font-weight: 800; font-size: 17px; line-height: 1.05; letter-spacing: 0.5px;
    color: var(--ink);
  }
  .person__name { font-weight: 700; font-size: 15px; color: var(--ink); }
  .person__role {
    font-weight: 400; font-size: 8px; letter-spacing: 0.4px;
    text-transform: uppercase; color: var(--muted); margin: 2px 0 14px;
  }
  .contacts { list-style: none; display: flex; flex-direction: column; gap: 7px; }
  .contacts__item {
    display: flex; align-items: center; gap: 8px;
    font-size: 10.5px; font-weight: 500; color: var(--ink);
  }
  .contacts__icon { width: 14px; height: 14px; flex: none; }
  .address {
    margin-top: 18px; font-size: 8.5px; line-height: 1.45;
    font-weight: 400; color: var(--muted); font-style: normal;
  }
  /* Back */
  .card--back {
    background: var(--charcoal);
    display: flex; align-items: center; justify-content: center;
  }
  .back__brand { display: flex; align-items: center; gap: 18px; }
  .back__square { width: 44px; height: 44px; background: var(--back-mark); }
  .back__name {
    font-weight: 800; font-size: 36px; line-height: 1.05; letter-spacing: 1px;
    color: var(--back-mark);
  }
</style>
</head>
<body>
<main class="stage">
  <section class="card card--front" aria-label="Business card front">
    <div class="front__panel" role="img" aria-label="Large brand symbol decoration in charcoal and white"></div>
    <div class="front__content">
      <div class="brand">
        <span class="brand__square"></span>
        <span class="brand__name">GREYHAVEN<br>CONTRACTS</span>
      </div>
      <p class="person__name">Kunal Mehra</p>
      <p class="person__role">Designated Partner</p>
      <ul class="contacts">
        <li class="contacts__item">
          <svg class="contacts__icon" viewBox="0 0 24 24" fill="none" stroke="currentColor" stroke-width="1.6" stroke-linecap="round" stroke-linejoin="round"><path d="M5 3h4l2 5-2.5 1.5a11 11 0 0 0 6 6L16 13l5 2v4a2 2 0 0 1-2 2A16 16 0 0 1 3 5a2 2 0 0 1 2-2z"/></svg>
          +91 97410 58723
        </li>
        <li class="contacts__item">
          <svg class="contacts__icon" viewBox="0 0 24 24" fill="none" stroke="currentColor" stroke-width="1.6" stroke-linejoin="round"><rect x="3" y="5" width="18" height="14" rx="1"/><path d="M3 6l9 7 9-7"/></svg>
          kunalmehra@examplemail.com
        </li>
        <li class="contacts__item">
          <svg class="contacts__icon" viewBox="0 0 24 24" fill="none" stroke="currentColor" stroke-width="1.6"><circle cx="12" cy="12" r="9"/><path d="M3 12h18M12 3c3 3 3 15 0 18M12 3c-3 3-3 15 0 18"/></svg>
          www.greyhavencontracts.example
        </li>
      </ul>
      <address class="address">
        Block No.317, Wing C, Tulsi Trade Plaza, Lokhand Marg,<br>
        Varun Industrial Park, Goregaon(E), Mumbai - 400 063
      </address>
    </div>
  </section>

  <section class="card card--back" aria-label="Business card back">
    <div class="back__brand">
      <span class="back__square"></span>
      <span class="back__name">GREYHAVEN<br>CONTRACTS</span>
    </div>
  </section>
</main>
</body>
</html>
```